ALL TEXT GRAPHICS TM May 2025 for Instagram

We are looking for a series of social media graphics for Instagram (new size: 4:5 (1080 x 1350 pixels) ratio that are ALL TEXT. We want the following quotes below on each graphic; one quote per graphic. AND, In very small letters at the bottom of each graphic, add @TovaMarshOnline
The look and feel of these graphics should be complimentary to the color palette attached below; but keep them simple. But the design is up to you; at the end of this document, I provided various samples of all text graphics that I like as examples.
Target Market(s)
women looking to lose weight
Look and feel

```html
<!DOCTYPE html>
<html lang="en">
<head>
<meta charset="UTF-8">
<title>Stubborn Weight Quote</title>
<link rel="stylesheet" href="https://fonts.googleapis.com/css2?family=Oswald:wght@600;700&family=Poppins:wght@400&display=swap">
<style>
  :root {
    --ink: #0c1b25;
    --accent: #cf0068;
    --frame: #ee2a8e;
    --blush: #fbb0d6;
    --paper: #ffffff;
  }
  * { margin: 0; padding: 0; box-sizing: border-box; }
  html, body {
    width: 960px;
    height: 1200px;
    overflow: hidden;
  }
  .card {
    position: relative;
    width: 960px;
    height: 1200px;
    background:
      radial-gradient(ellipse 520px 520px at 0% 0%, var(--blush) 0%, rgba(251,176,214,0.55) 30%, rgba(255,255,255,0) 75%),
      radial-gradient(ellipse 560px 560px at 100% 100%, var(--blush) 0%, rgba(251,176,214,0.55) 30%, rgba(255,255,255,0) 75%),
      radial-gradient(ellipse 420px 300px at 0% 70%, rgba(251,176,214,0.35) 0%, rgba(255,255,255,0) 80%),
      var(--paper);
  }
  .card-frame {
    position: absolute;
    left: 19px;
    top: 19px;
    right: 19px;
    bottom: 19px;
    border: 2px solid var(--frame);
  }
  .quote {
    position: absolute;
    left: 134px;
    top: 213px;
    font-family: "Oswald", sans-serif;
    font-weight: 700;
    font-size: 91px;
    line-height: 92.5px;
    text-transform: uppercase;
    color: var(--ink);
    letter-spacing: -0.5px;
  }
  .quote-line {
    display: block;
    white-space: nowrap;
  }
  .highlight { color: var(--accent); }
  .handle {
    position: absolute;
    left: 0;
    right: 0;
    top: 1109px;
    text-align: center;
    font-family: "Poppins", sans-serif;
    font-weight: 400;
    font-size: 24px;
    color: var(--ink);
  }
</style>
</head>
<body>
  <main class="card">
    <div class="card-frame"></div>
    <h1 class="quote">
      <span class="quote-line">That <span class="highlight">stubborn</span></span>
      <span class="quote-line"><span class="highlight">weight?</span> It’s not</span>
      <span class="quote-line">your fault.</span>
      <span class="quote-line">Your <span class="highlight">hormones</span></span>
      <span class="quote-line"><span class="highlight">are</span> to blame</span>
      <span class="quote-line">and <span class="highlight">you’re</span> not</span>
      <span class="quote-line"><span class="highlight">alone</span>; but</span>
      <span class="quote-line">there is a fix.</span>
    </h1>
    <p class="handle">@TovaMarshOnline</p>
  </main>
</body>
</html>
```